Web page design for podiatry office*

Need a web page for our podiatry office. It should feature most of our services, hours, directions and location. Should include a short bio of the doctor and a contact page.

Coding

Coded - Design and coding required

Number of Pages Required

1 page

Colors

Designer to choose colors to be used in the design.

```html
<!DOCTYPE html>
<html lang="en">
<head>
<meta charset="utf-8">
<title>Stride Foot Clinic</title>
<link href="https://fonts.googleapis.com/css2?family=Montserrat:wght@500;600;700;800&family=Lato:wght@400;700&family=Roboto:wght@400;500&display=swap" rel="stylesheet">
<style>
:root{
  --blue:#2a86db;
  --orange:#fb6a0c;
  --ink:#333a44;
  --muted:#555;
  --light:#f8f8f8;
  --grey-bar:#ededed;
  --contact-left:#8d8d8d;
  --contact-right:#e7e7e7;
  --footer:#13202f;
  --white:#fff;
}
*{margin:0;padding:0;box-sizing:border-box}
html,body{width:1200px;height:2580px;overflow:hidden}
body{position:relative;background:var(--white);font-family:'Lato',sans-serif;color:var(--ink)}
.abs{position:absolute}
.topbar{left:0;top:0;width:1200px;height:25px;background:var(--grey-bar);font-size:10px}
.topbar .news{left:233px;top:7px;font-weight:700;color:#222}
.topbar .news span{font-weight:400;font-size:8px;margin-left:3px}
.topbar .phone{left:762px;top:7px;font-size:9px}
.topbar .reg{left:865px;top:7px;font-size:9px}
.topbar .login{left:924px;top:0;width:39px;height:25px;background:var(--blue);color:#fff;font-size:9px;text-align:center;line-height:25px}
.header{left:0;top:25px;width:1200px;height:63px;border-bottom:3px solid var(--blue)}
.brand{left:233px;top:20px;display:flex;align-items:center;gap:6px;font-family:'Montserrat',sans-serif;font-weight:700;font-size:17px;color:var(--blue);white-space:nowrap}
.brand i{width:11px;height:11px;border-radius:50%;background:var(--blue);display:block}
.footer .brand{font-size:14px;gap:5px}
.footer .brand i{width:9px;height:9px}
.nav{left:600px;top:26px;display:flex;gap:22px;font-family:'Montserrat',sans-serif;font-size:9px;font-weight:500;color:#333}
.nav .on{color:var(--blue)}
.cta{left:857px;top:19px;width:106px;height:24px;background:var(--orange);color:#fff;font-family:'Montserrat',sans-serif;font-size:8.5px;font-weight:600;text-align:center;line-height:24px}
.hero{left:0;top:91px;width:1200px;height:410px;background:linear-gradient(100deg,#e4edf5 0%,#d7e2ec 45%,#c9b29e 60%,#e9eef3 85%)}
.hero-text{left:272px;top:206px}
.hero-text .kicker{font-family:'Montserrat',sans-serif;color:var(--blue);font-size:15px;font-weight:600;letter-spacing:.5px}
.hero-text h1{font-family:'Montserrat',sans-serif;font-weight:800;color:var(--orange);font-size:30px;margin-top:10px}
.hero-text p{font-family:'Roboto',sans-serif;font-size:12px;line-height:17.5px;color:#333;width:355px;margin-top:18px}
.btn-blue{display:inline-block;background:var(--blue);color:#fff;font-family:'Montserrat',sans-serif;font-size:9px;font-weight:600;width:103px;height:28px;line-height:28px;text-align:center;margin-top:24px}
.arrow{width:34px;height:34px;border-radius:50%;background:rgba(255,255,255,.4)}
h2.sec{font-family:'Montserrat',sans-serif;font-weight:700;font-size:20px;color:var(--blue)}
h2.sec span{color:var(--orange)}
.rule{width:28px;height:2px;background:var(--blue)}
.svc{width:156px;height:147px;background:var(--light);text-align:center;font-size:12px;color:#333}
.svc svg{margin-top:40px}
.svc .ln{width:24px;height:1px;background:var(--blue);margin:7px auto 10px;opacity:.6}
.svc.on{background:var(--blue);color:#fff}
.svc.on .ln{background:#fff}
.appt{left:733px;top:504px;width:230px;height:345px;background:var(--blue);color:#fff;text-align:center}
.appt h3{font-family:'Montserrat',sans-serif;font-size:13px;font-weight:600;margin-top:36px}
.appt small{display:block;font-size:8px;font-weight:700;margin-top:6px}
.field{width:193px;height:26px;background:#fff;margin:8px auto 0;color:#aaa;font-size:8px;text-align:left;padding-left:12px;line-height:26px;position:relative}
.field:after{content:"";position:absolute;right:12px;top:11px;border:4px solid transparent;border-top-color:#999}
.field.ic:after{border:1px solid #bbb;border-radius:50%;width:6px;height:6px;top:9px}
.appt .note{font-size:8px;text-align:left;margin:18px 0 0 18px}
.appt .submit{width:193px;height:31px;border:1px solid #fff;margin:9px auto 0;font-family:'Montserrat',sans-serif;font-size:8.5px;font-weight:600;line-height:30px}
.doc-photo{left:235px;top:1075px;width:260px;height:423px;background:linear-gradient(180deg,#dfe8f0 0%,#4f7fc4 40%,#2b58a6 100%);border-radius:100px 100px 0 0}
.bio{left:609px;top:1050px;width:345px}
.bio p{font-size:9.5px;line-height:15px;color:#444;margin:0 0 15px 4px}
.qual{list-style:none;font-family:'Roboto',sans-serif;font-size:10px;margin-top:28px}
.qual li{height:18.7px;display:flex;align-items:center}
.qual li:before{content:"";border:5px solid transparent;border-left:8px solid var(--orange);margin-right:7px}
.qual b{width:90px;font-weight:500;color:#111}
.band{left:0;top:1498px;width:1200px;height:347px;background:var(--blue);color:#fff}
.band h2{font-family:'Montserrat',sans-serif;font-size:20px;font-weight:700}
.band h2 span{color:var(--orange)}
.band .rule{background:#fff}
.map{left:237px;top:1601px;width:446px;height:196px;background:linear-gradient(135deg,#e9e9e4,#f3eedd 50%,#e6e6e6);border:6px solid #a8b4c2}
.addr{left:722px;top:1608px;font-family:'Roboto',sans-serif;font-size:15.5px;line-height:28.5px;font-weight:500;color:#fff}
.btn-orange{background:var(--orange);color:#fff;font-family:'Montserrat',sans-serif;font-weight:600;text-align:center}
.cleft{left:0;top:1845px;width:599px;height:460px;background:var(--contact-left);color:#fff}
.cright{left:599px;top:1845px;width:601px;height:460px;background:var(--contact-right)}
.cleft h2{position:absolute;left:235px;top:58px;font-family:'Montserrat',sans-serif;font-weight:800;color:#111;font-size:28px}
.cleft p{position:absolute;left:240px;top:106px;width:330px;font-family:'Roboto',sans-serif;font-size:11.5px;line-height:19px}
.cleft h4{position:absolute;left:235px;top:188px;font-family:'Roboto',sans-serif;font-weight:400;font-size:20px}
.crow{position:absolute;left:235px;display:flex;align-items:center;gap:17px;font-family:'Roboto',sans-serif;font-size:12px;color:#111}
.flabel{position:absolute;left:66px;font-size:8.5px;color:var(--blue);font-family:'Roboto',sans-serif}
.fline{position:absolute;left:66px;width:243px;height:1px;background:var(--blue)}
.footer{left:0;top:2305px;width:1200px;height:275px;background:var(--footer);color:#fff;border-top:2px solid var(--blue)}
.footer h5{position:absolute;top:48px;font-family:'Montserrat',sans-serif;font-size:11.5px;font-weight:700}
.footer h5 span{color:var(--blue)}
.footer ul{position:absolute;top:84px;list-style:none;font-size:8.5px}
.links li{height:22.5px}
.links li:before{content:"› ";color:var(--blue)}
.contacts li{height:26.5px;display:flex;gap:7px;align-items:flex-start}
.hours li{height:18.8px;display:flex;align-items:center}
.hours li .d{width:50px}
.hours li .dash{width:32px;height:1px;background:#444;margin:0 15px 0 0}
.social{position:absolute;left:233px;top:201px;display:flex;gap:10px}
.social i{width:15px;height:15px;background:#fff;display:block}
.social i.b{background:var(--blue)}
.copy{position:absolute;left:233px;top:250px;font-size:8.5px;color:#bbb}
.fnav{position:absolute;left:830px;top:250px;font-size:8.5px;color:#bbb;display:flex;gap:11px}
.totop{left:938px;top:2306px;width:25px;height:24px;background:var(--blue)}
</style>
</head>
<body>

<div class="abs topbar">
  <div class="abs news">Hot News ! <span>Lorem ipsum dolar set ament</span></div>
  <div class="abs phone">&#9647; +00 555-010-2480</div>
  <div class="abs reg">REGISTER</div>
  <div class="abs login">LOGIN</div>
</div>

<header class="abs header">
  <div class="abs brand"><i></i>Stride Foot Clinic</div>
  <nav class="abs nav"><span class="on">HOME</span><span>SERVICES</span><span>ABOUT</span><span>BLOG</span><span>PAGES</span></nav>
  <div class="abs cta">MAKE APPOINTMENT</div>
</header>

<div class="abs hero" role="img" aria-label="Photo of a podiatrist in white gloves examining a patient's foot"></div>
<div class="abs arrow" style="left:227px;top:228px"></div>
<div class="abs arrow" style="left:934px;top:228px"></div>
<svg class="abs" style="left:0;top:230px" width="1200" height="40"><path d="M245 15 H258 M251 9 L245 15 L251 21 M948 15 H962 M956 9 L962 15 L956 21" stroke="#555" stroke-width="1.3" fill="none"/></svg>
<div class="abs hero-text">
  <div class="kicker">WE PROVIDE</div>
  <h1>Podiatry Services</h1>
  <p>Lorem ipsum dolor sit amet, consectetur adipisicing elit, sed do eius­mod tempor incididunt ut labore et dolore magna aliqua. Ut enim ali­quam quaerat voluptatem.</p>
  <span class="btn-blue">READ MORE</span>
</div>
<svg class="abs" style="left:0;top:400px" width="1200" height="110">
  <path d="M0 45 Q330 0 600 88 Q870 0 1200 45 V110 H0 Z" fill="#fff"/>
  <path d="M0 40 Q330 -5 600 88 Q870 -5 1200 40" stroke="#2a86db" stroke-width="9" fill="none"/>
  <circle cx="600" cy="89" r="11" fill="#2a86db"/>
</svg>

<h2 class="abs sec" style="left:236px;top:500px">OUR <span>SERVICES</span></h2>
<div class="abs rule" style="left:238px;top:536px"></div>

<div class="abs svc" style="left:233px;top:548px">
  <svg width="30" height="30" viewBox="0 0 30 30" fill="none" stroke="#666" stroke-width="1.2"><rect x="4" y="10" width="20" height="9" rx="4.5" transform="rotate(-50 14 14)"/><circle cx="21" cy="21" r="6"/></svg>
  <div class="ln"></div>Medicine &amp; Drug Store</div>
<div class="abs svc on" style="left:395px;top:548px">
  <svg width="30" height="30" viewBox="0 0 30 30" fill="none" stroke="#fff" stroke-width="1.2"><path d="M12 10 C8 16 12 20 11 26 C13 29 18 28 18 24 C17 20 20 16 19 11 Z"/><circle cx="10" cy="5" r="1.5"/><circle cx="14" cy="4" r="1.5"/><circle cx="18" cy="5" r="1.5"/></svg>
  <div class="ln"></div>Podiatry Services</div>
<div class="abs svc" style="left:557px;top:548px">
  <svg width="30" height="30" viewBox="0 0 30 30" fill="none" stroke="#666" stroke-width="1.2"><path d="M15 26 L4 14 C0 8 8 2 15 9 C22 2 30 8 26 14 Z"/><path d="M5 15 H11 L13 11 L16 18 L18 14 H25"/></svg>
  <div class="ln"></div>Speacial Health Care</div>
<div class="abs svc" style="left:233px;top:702px">
  <svg width="30" height="30" viewBox="0 0 30 30" fill="none" stroke="#666" stroke-width="1.2"><path d="M3 27 L8 22 M8 22 L20 10 L24 14 L12 26 Z M22 8 L26 12 M24 6 L28 10"/></svg>
  <div class="ln"></div>Operation Section</div>
<div class="abs svc" style="left:395px;top:702px">
  <svg width="34" height="30" viewBox="0 0 34 30" fill="none" stroke="#666" stroke-width="1.2"><path d="M4 6 C2 14 10 24 18 26 L21 22 L16 18 L13 20 C10 17 8 15 7 12 L10 9 L7 4 Z"/><circle cx="24" cy="10" r="7"/><path d="M24 6 V14 M20 10 H28"/></svg>
  <div class="ln"></div>Emergency Help</div>
<div class="abs svc" style="left:557px;top:702px">
  <svg width="30" height="30" viewBox="0 0 30 30" fill="none" stroke="#666" stroke-width="1.2"><path d="M6 3 V13 C6 19 14 19 14 13 V3 M10 18 V24 C10 28 20 28 20 22 V17"/><circle cx="20" cy="14" r="3"/></svg>
  <div class="ln"></div>Speacial Check up</div>

<div class="abs appt">
  <h3>MAKE AN APPOINTMENT</h3>
  <small>FILL FORM &amp; SEND ME</small>
  <div class="field" style="margin-top:16px">Select your country</div>
  <div class="field">Choose Services</div>
  <div class="field">Select Doctor</div>
  <div class="field ic">Choose Date</div>
  <div class="field ic">Select Time</div>
  <div class="note">All Fields With an Are Required ***</div>
  <div class="submit">SUBMIT YOU REQUIREMENTS</div>
</div>

<svg class="abs" style="left:0;top:900px" width="1200" height="100">
  <path d="M0 40 Q330 -5 600 86 Q870 -5 1200 40" stroke="#2a86db" stroke-width="9" fill="none"/>
  <circle cx="600" cy="86" r="11" fill="#2a86db"/>
</svg>

<div class="abs doc-photo" role="img" aria-label="Photo of the doctor in blue scrubs and surgical cap, arms crossed"></div>

<div class="abs bio">
  <h2 class="sec">DOCTOR'S <span>BIOGRAPHY</span></h2>
  <div class="rule" style="margin:14px 0 24px 2px"></div>
  <p>Lorem ipsum dolor sit amet, consectetur adipiscing elit, sed do eiusmod tempor incididunt ut labore et dolore magna aliqua. Ut enim ad minim veniam, quis nos­trud exercitation ullamco laboris nisi ut aliquip ex ea commodo consequat.</p>
  <p>Lorem ipsum dolor sit amet, consectetur adipiscing elit, sed do eiusmod tempor incididunt ut labore et dolore magna aliqua. Ut enim ad minim veniam, quis nos­trud exercitation ullamco laboris nisi ut aliquip ex ea commodo consequat.</p>
  <p>Lorem ipsum dolor sit amet, consectetur adipiscing elit, sed do eiusmod tempor incididunt ut labore et dolore magna aliqua. Ut enim ad minim veniam, quis nos­trud exercitation ullamco laboris nisi ut aliquip ex ea commodo consequat.</p>
  <h2 class="sec" style="margin-top:22px">DOCTOR'S <span>QUALIFICATIONS</span></h2>
  <div class="rule" style="margin:14px 0 0 2px"></div>
  <ul class="qual">
    <li><b>NAME:</b>Daniel Hart</li>
    <li><b>AGE:</b>45years</li>
    <li><b>DEGREE:</b>FRCS(LONDON)</li>
    <li><b>EXPERIENCE:</b>2 years</li>
    <li><b>COUNTRY:</b>USA</li>
    <li><b>WORK NOW:</b>Stride Foot Clinic</li>
  </ul>
</div>

<section class="abs band">
  <h2 class="abs" style="left:240px;top:46px">STRIDEFOOTCLINIC <span>LOCATION</span></h2>
  <div class="abs rule" style="left:242px;top:84px"></div>
  <h2 class="abs" style="left:720px;top:46px">STRIDEFOOTCLINIC <span>DIRECTION</span></h2>
  <div class="abs rule" style="left:723px;top:84px"></div>
</section>
<div class="abs map" role="img" aria-label="Street map of downtown Los Angeles showing the clinic area"></div>
<div class="abs addr">Demo Road 123 Street,<br>Losangels 652,<br>Zip Code 123456<br>USA</div>
<div class="abs btn-orange" style="left:724px;top:1749px;width:108px;height:27px;line-height:27px;font-size:10.5px">GET DIRECTION</div>

<section class="abs cleft">
  <h2>CONTACT US</h2>
  <p>Lorem ipsum dolor sit amet, consectetur adipiscing elit, sed do eiusmod tempor incididunt ut labore et dolore magna aliqua.</p>
  <h4>StrideFootClinic</h4>
  <div class="crow" style="top:234px"><svg width="17" height="15"><rect width="17" height="15" rx="2" fill="#fff"/><path d="M5 3 C4 8 8 12 12 12 L12 10 L10 9 L9 10 C8 9 7 8 6 7 L7 6 L6 3 Z" fill="#888"/></svg>+1 (555) 010-XXXXX</div>
  <div class="crow" style="top:257px"><svg width="17" height="15" fill="none" stroke="#fff" stroke-width="1.3"><rect x="1" y="2" width="15" height="11"/><path d="M1 2 L8.5 8 L16 2"/></svg>hello@stridefootclinic.com</div>
  <div class="crow" style="top:280px"><svg width="17" height="18"><path d="M3 1 V15 L7 11 L10 17 L12 16 L9 10 H14 Z" fill="#fff"/></svg> www.stridefootclinic.com</div>
</section>
<section class="abs cright">
  <div class="flabel" style="top:110px">Name</div><div class="fline" style="top:132px"></div>
  <div class="flabel" style="top:160px">Email</div><div class="fline" style="top:182px"></div>
  <div class="flabel" style="top:210px">Subject</div><div class="fline" style="top:232px"></div>
  <div class="flabel" style="top:248px">Message</div><div class="fline" style="top:337px;left:64px"></div>
  <div class="abs btn-orange" style="left:65px;top:364px;width:107px;height:33px;line-height:33px;font-size:13px">SEND</div>
</section>

<footer class="abs footer">
  <div class="abs brand" style="top:66px;left:235px"><i></i>Stride Foot Clinic</div>
  <p style="position:absolute;left:233px;top:103px;width:170px;font-size:8.5px;line-height:15px">Lorem ipsum dolor sit amet, consectetur adipiscing elit, sed do eiusmod tempor incididunt ut labore et dolore magna aliqua. Ut enim ad minim veniam, quis nostrud exercitation ullamco laboris nisi ut</p>
  <div class="social"><i></i><i class="b"></i><i></i><i></i><i></i></div>
  <h5 style="left:421px"><span>QUICK</span> LINKS</h5>
  <ul class="links" style="left:421px"><li>Healthcare Programe</li><li>Family Treatment</li><li style="color:var(--blue)">Medical Injuries</li><li>Personal Doctor</li><li>Operations</li></ul>
  <h5 style="left:609px"><span>CONTACT</span> US</h5>
  <ul class="contacts" style="left:609px">
    <li><svg width="8" height="10"><path d="M4 10 C1 6 0 4.5 0 3.5 A4 4 0 0 1 8 3.5 C8 4.5 7 6 4 10 Z" fill="#2a86db"/></svg>Demo Road, Losangels, USA</li>
    <li><svg width="9" height="8" fill="none" stroke="#2a86db"><rect x=".5" y=".5" width="8" height="7"/></svg>contact@stridefootclinic.com</li>
    <li><svg width="9" height="9" fill="none" stroke="#2a86db" stroke-width="1.3"><path d="M1 7 V5 A3.5 3.5 0 0 1 8 5 V7"/></svg>( +00 ) 55-01-02-222</li>
    <li><svg width="9" height="9" fill="none" stroke="#2a86db" stroke-width="1.3"><path d="M1 7 V5 A3.5 3.5 0 0 1 8 5 V7"/></svg>( +00 ) 55-01-03-888</li>
  </ul>
  <h5 style="left:795px"><span>WORKING</span> HOURS</h5>
  <ul class="hours" style="left:796px;top:82px">
    <li><span class="d">Monday</span><span class="dash"></span>9:00 am - 8:00 pm</li>
    <li><span class="d">Tuesday</span><span class="dash"></span>9:00 am - 8:00 pm</li>
    <li><span class="d">Wednesday</span><span class="dash"></span>9:00 am - 8:00 pm</li>
    <li><span class="d">Thursday</span><span class="dash"></span>9:00 am - 8:00 pm</li>
    <li><span class="d">Friday</span><span class="dash"></span>9:00 am - 8:00 pm</li>
    <li><span class="d">Saturday</span><span class="dash"></span>9:00 am - 8:00 pm</li>
  </ul>
  <div class="copy">stridefootclinic.com © 2019, All Rights Reserved</div>
  <div class="fnav"><span>Home</span><span>About</span><span>Blog</span><span>Contact us</span></div>
</footer>
<div class="abs totop"><svg width="25" height="24"><path d="M10 13 L12.5 10.5 L15 13" stroke="#fff" stroke-width="1.3" fill="none"/></svg></div>

</body>
</html>
```